Business Card Design

We need a design for business cards for our company. We have a logo. We teach EMT's and we are based out of Virginia. The information that will need to add would be, name, title, phone number, email, address. On the back of the business card would be "We help you, help others"

Target Market(s)

People that want to become EMT's

Colors

Designer to choose colors to be used in the design.

Requirements
Must have
• company logo

```html
<!DOCTYPE html>
<html lang="en">
<head>
<meta charset="utf-8">
<title>Business Card – Front and Back</title>
<link rel="stylesheet" href="https://fonts.googleapis.com/css2?family=Roboto:wght@400;500&family=Montserrat:wght@600&family=Crimson+Pro:ital,wght@1,500&display=swap">
<style>
  :root {
    --backdrop: #2b2b2b;
    --card-white: #ffffff;
    --brand-red: #be1e2d;
    --brand-red-deep: #a51826;
    --ink: #222222;
    --rule: #8a8a8a;
  }
  * { box-sizing: border-box; margin: 0; padding: 0; }
  html, body { width: 1200px; height: 1200px; overflow: hidden; }
  body { background: var(--backdrop); position: relative; }

  .card {
    position: absolute;
    top: 310px;
    width: 366px;
    height: 594px;
    box-shadow: 0 4px 12px rgba(0,0,0,0.45);
  }
  .card--front { left: 233px; background: var(--card-white); }
  .card--back  { left: 628px; background: var(--brand-red); overflow: hidden; }

  .brand {
    position: absolute;
    top: 150px;
    left: 0; right: 0;
    display: flex;
    align-items: center;
    justify-content: center;
    gap: 12px;
  }
  .brand__mark { width: 30px; height: 30px; background: var(--brand-red); flex: none; }
  .brand__name {
    font-family: "Montserrat", sans-serif;
    font-weight: 600;
    font-size: 23px;
    line-height: 1.1;
    color: var(--brand-red);
    letter-spacing: 0.5px;
  }

  .contact {
    position: absolute;
    top: 382px;
    left: 0; right: 0;
    text-align: center;
    font-family: "Roboto", sans-serif;
    color: var(--ink);
    font-size: 16.5px;
    line-height: 22px;
  }
  .contact__name {
    font-weight: 500;
    font-size: 22px;
    line-height: 26px;
    color: var(--brand-red);
    text-transform: uppercase;
  }
  .contact__rule {
    width: 162px;
    height: 1px;
    background: var(--rule);
    margin: 10px auto 8px;
  }

  .tagline {
    position: absolute;
    top: 150px;
    left: 0; right: 0;
    text-align: center;
    font-family: "Crimson Pro", serif;
    font-style: italic;
    font-weight: 500;
    font-size: 74px;
    line-height: 106px;
    color: var(--card-white);
  }
  .back-accent {
    position: absolute;
    left: 240px;
    top: 452px;
    width: 118px;
    height: 118px;
    background: var(--brand-red-deep);
    opacity: 0.6;
  }
</style>
</head>
<body>
  <section class="card card--front">
    <div class="brand">
      <span class="brand__mark"></span>
      <span class="brand__name">BRIGHTLINE<br>MEDIC TRAINING</span>
    </div>
    <div class="contact">
      <p class="contact__name">Daniel Hartley</p>
      <p class="contact__title">Managing Director</p>
      <div class="contact__rule"></div>
      <p class="contact__phone">055-987 654 321</p>
      <p class="contact__email">hello@brightline.com</p>
      <div class="contact__rule"></div>
      <p class="contact__address">17, Harbor Lane, Suite 4</p>
      <p class="contact__address">23220, Virginia</p>
    </div>
  </section>

  <section class="card card--back">
    <div class="back-accent"></div>
    <p class="tagline">We help<br>you, help<br>others</p>
  </section>
</body>
</html>
```